Construction Company Business Card

We need a logo and a business card for our new construction company. We are based in Nairobi, Kenya. Our company specializes in the design and construction of high end residential homes and commercial buildings. We want a modern and elegant logo. Preferred colours are gun metal grey/ slate (or anything along those lines) and red as a feature. We are however open to any ideas. The design should communicate prestige and elegance in the work that we undertake.
The uploaded sketch is just something we were pondering with but you can completely disregard it.

Industry/Entity Type

Construction

Contact Information for Business Card

Company Name: Tabor Vask

Company Address:
Tabor Vask
P.O.Box 2871-00529
Ruaraka, Nairobi, 00529
Kenya

Name on business card: Tabor V. Osumba

```html
<!DOCTYPE html>
<html lang="en">
<head>
<meta charset="utf-8">
<title>Tabor Vask — Business Card</title>
<link rel="stylesheet" href="https://fonts.googleapis.com/css2?family=Open+Sans:wdth,wght@75..100,400;75..100,600&display=swap">
<style>
  :root {
    --card-slate: #5d6370;
    --card-edge: #2f3236;
    --panel-white: #ffffff;
    --ink-black: #0d0d0d;
    --ink-cyan: #6ff3f3;
    --brand-slate: #6e7c7c;
    --brand-red: #e8101a;
  }
  html, body {
    margin: 0;
    padding: 0;
    width: 1200px;
    height: 900px;
    overflow: hidden;
    background: var(--card-slate);
  }
  .card {
    position: relative;
    width: 1200px;
    height: 900px;
    box-sizing: border-box;
    border: 3px solid var(--card-edge);
    background: var(--card-slate);
    font-family: "Open Sans", "Segoe UI", sans-serif;
  }
  .brand-panel {
    position: absolute;
    left: 79px;
    top: 83px;
    width: 439px;
    height: 725px;
    background: var(--panel-white);
    display: flex;
    flex-direction: column;
    align-items: center;
    justify-content: center;
    gap: 44px;
  }
  .brand-mark {
    width: 150px;
    height: 150px;
    background: var(--brand-red);
  }
  .brand-name {
    margin: 0;
    font-size: 150px;
    font-weight: 600;
    font-stretch: 80%;
    line-height: 0.98;
    text-align: center;
    color: var(--brand-slate);
  }
  .brand-name span { display: block; }
  .holder-name {
    position: absolute;
    left: 694px;
    top: 137px;
    margin: 0;
    font-size: 68px;
    font-weight: 400;
    font-stretch: 82%;
    line-height: 1;
    color: var(--ink-black);
    white-space: nowrap;
  }
  .address {
    position: absolute;
    left: 522px;
    top: 368px;
    width: 612px;
    margin: 0;
    font-style: normal;
    text-align: center;
    font-size: 55px;
    font-weight: 400;
    font-stretch: 88%;
    line-height: 78px;
    color: var(--ink-cyan);
  }
  .address span { display: block; white-space: nowrap; }
</style>
</head>
<body>
  <div class="card">
    <div class="brand-panel">
      <span class="brand-mark" aria-hidden="true"></span>
      <p class="brand-name"><span>Tabor</span><span>Vask</span></p>
    </div>

    <h1 class="holder-name">Tabor V. Osumba</h1>

    <address class="address">
      <span>Tabor Vask</span>
      <span>Post Box: 2871-00529</span>
      <span>Ruaraka</span>
      <span>Nairobi - 00529</span>
      <span>Kenya</span>
    </address>
  </div>
</body>
</html>
```